Rocket business card

Modern business card design, use of color is good with clean space too.

Things to include on card:

Quote: I add fuel to your optometry practice

- Eyewear Sales
- Admin Duties
- Revenue Collection
- Leadership
- Tech Adoption
- COGS Reduction
- Product Sourcing
-Medical Growth

Dalton Vessey, CEO
Glint Harbor
Text Me! 847-302-1964
dalton@glintharbor.example

```html
<!DOCTYPE html>
<html lang="en">
<head>
<meta charset="utf-8">
<title>Glint Harbor — Business Card</title>
<link href="https://fonts.googleapis.com/css2?family=Lato:wght@300;400;700&display=swap" rel="stylesheet">
<style>
  :root {
    --stage: #2f3533;
    --card-dark-start: #4a4a4a;
    --card-dark-end: #1c1c1c;
    --card-light: #f7f7f7;
    --ink: #111111;
    --ink-soft: #4d4d4d;
    --ink-muted: #6a6a6a;
    --on-dark: #e6e6e6;
    --on-dark-muted: #b5b5b5;
    --accent: #e8663d;
    --accent-end: #f0923a;
  }
  * { box-sizing: border-box; margin: 0; padding: 0; }
  html, body {
    width: 1200px; height: 1200px; overflow: hidden;
    background: var(--stage);
    font-family: "Lato", sans-serif;
  }
  .stage {
    width: 1200px; height: 1200px;
    display: flex; flex-direction: column;
    align-items: center; justify-content: center;
    gap: 64px;
  }
  .card {
    width: 760px; height: 434px;
    position: relative;
    box-shadow: 0 18px 40px rgba(0,0,0,.35);
  }
  .brand { display: flex; align-items: center; gap: 18px; }
  .brand__dot {
    border-radius: 50%;
    background: linear-gradient(135deg, var(--accent), var(--accent-end));
    flex: none;
  }
  .brand__name {
    font-weight: 400;
    text-transform: uppercase;
    white-space: nowrap;
  }

  /* Back side */
  .card--back {
    background: linear-gradient(110deg, var(--card-dark-start), var(--card-dark-end) 70%);
    display: flex; flex-direction: column;
    align-items: center; justify-content: center;
    gap: 26px;
    padding: 0 48px;
  }
  .card--back .brand__dot { width: 64px; height: 64px; }
  .card--back .brand__name { color: var(--on-dark); font-size: 40px; letter-spacing: 4px; }
  .quote {
    color: var(--on-dark);
    font-size: 19px; font-weight: 300;
    letter-spacing: .3px;
  }
  .quote::before, .quote::after { color: var(--accent-end); font-weight: 700; }
  .quote::before { content: "\201C"; margin-right: 2px; }
  .quote::after  { content: "\201D"; margin-left: 2px; }
  .services {
    list-style: none;
    display: grid;
    grid-template-columns: repeat(4, auto);
    column-gap: 28px; row-gap: 10px;
  }
  .services__item {
    display: flex; align-items: center; gap: 8px;
    color: var(--on-dark-muted);
    font-size: 15px; font-weight: 400;
    white-space: nowrap;
  }
  .services__item::before {
    content: ""; width: 6px; height: 6px; border-radius: 50%;
    background: var(--accent); flex: none;
  }
  .card--back .website {
    color: var(--on-dark);
    font-size: 17px; font-weight: 400;
    letter-spacing: .5px;
  }

  /* Front side */
  .card--front {
    background: var(--card-light);
    padding: 0 56px;
    display: flex; align-items: center; justify-content: space-between;
  }
  .identity { display: flex; flex-direction: column; }
  .identity__name {
    font-size: 28px; font-weight: 700; color: var(--ink-soft);
    text-transform: uppercase; letter-spacing: .5px;
  }
  .identity__title {
    font-size: 18px; font-weight: 300; color: var(--ink-muted);
    margin-top: 2px; margin-bottom: 24px;
  }
  .contact { list-style: none; display: flex; flex-direction: column; gap: 10px; }
  .contact__item {
    display: flex; align-items: center; gap: 12px;
    font-size: 17px; color: var(--ink-muted); font-weight: 400;
    white-space: nowrap;
  }
  .contact__label { font-weight: 700; color: var(--ink-soft); }
  .contact__icon { width: 17px; height: 17px; flex: none; }
  .card--front .brand__dot { width: 50px; height: 50px; }
  .card--front .brand__name { color: var(--ink); font-size: 30px; letter-spacing: 2px; }
</style>
</head>
<body>
<main class="stage">
  <section class="card card--back" aria-label="Card back">
    <div class="brand">
      <span class="brand__dot"></span>
      <span class="brand__name">Glint Harbor</span>
    </div>
    <p class="quote">I add fuel to your optometry practice</p>
    <ul class="services">
      <li class="services__item">Eyewear Sales</li>
      <li class="services__item">Admin Duties</li>
      <li class="services__item">Revenue Collection</li>
      <li class="services__item">Leadership</li>
      <li class="services__item">Tech Adoption</li>
      <li class="services__item">COGS Reduction</li>
      <li class="services__item">Product Sourcing</li>
      <li class="services__item">Medical Growth</li>
    </ul>
    <p class="website">www.glintharbor.example</p>
  </section>

  <section class="card card--front" aria-label="Card front">
    <div class="identity">
      <h1 class="identity__name">Dalton Vessey</h1>
      <p class="identity__title">CEO</p>
      <ul class="contact">
        <li class="contact__item">
          <svg class="contact__icon" viewBox="0 0 24 24" fill="#6a6a6a"><path d="M6.6 10.8a15.1 15.1 0 0 0 6.6 6.6l2.2-2.2c.3-.3.7-.4 1-.2 1.1.4 2.3.6 3.6.6.6 0 1 .4 1 1V20c0 .6-.4 1-1 1A17 17 0 0 1 3 4c0-.6.4-1 1-1h3.5c.6 0 1 .4 1 1 0 1.3.2 2.5.6 3.6.1.3 0 .7-.2 1z"/></svg>
          <span><span class="contact__label">Text Me!</span> 847-302-1964</span>
        </li>
        <li class="contact__item">
          <svg class="contact__icon" viewBox="0 0 24 24"><path d="M2 5h20v14H2z M2 5l10 8 10-8" fill="none" stroke="#6a6a6a" stroke-width="2"/></svg>
          dalton@glintharbor.example
        </li>
        <li class="contact__item">
          <svg class="contact__icon" viewBox="0 0 24 24"><circle cx="12" cy="12" r="9" fill="none" stroke="#6a6a6a" stroke-width="2"/><path d="M3 12h18M12 3c3 3 3 15 0 18M12 3c-3 3-3 15 0 18" fill="none" stroke="#6a6a6a" stroke-width="1.5"/></svg>
          www.glintharbor.example
        </li>
      </ul>
    </div>
    <div class="brand">
      <span class="brand__dot"></span>
      <span class="brand__name">Glint Harbor</span>
    </div>
  </section>
</main>
</body>
</html>
```